Garden Design Flier

I would like a PDF of this half page A4 flier in soft green tones with dark green leaves.

Target Market(s)

Home owners and real estate agents

Font styles to use
Serif
Other font styles liked:
• Papyrus

Colors
acd136
9bcb3c
cadf82
fefdec

Requirements
Must have
• Green tones
Nice to have
• Leaves, vines, lawns
Should not have
• Open to ideas, but classic style

```html
<!DOCTYPE html>
<html lang="en">
<head>
<meta charset="utf-8">
<title>Parterre Gardens – Flier</title>
<link rel="stylesheet" href="https://fonts.googleapis.com/css2?family=Bebas+Neue&family=Kaushan+Script&family=Montserrat:wght@500;600;700;800&display=swap">
<style>
  :root {
    --leaf-bg: #a7d47d;
    --leaf-bg-light: #b4db8f;
    --leaf-bg-deep: #97c96b;
    --forest: #0f3300;
    --forest-text: #123d00;
    --ink-green: #1d4410;
    --lime: #8cf20c;
    --white: #ffffff;
  }
  html, body {
    margin: 0;
    padding: 0;
    width: 1200px;
    height: 848px;
    overflow: hidden;
  }
  body {
    font-family: "Montserrat", sans-serif;
    color: var(--forest-text);
  }
  .flier {
    position: relative;
    width: 1200px;
    height: 848px;
    overflow: hidden;
  }
  .foliage-backdrop {
    position: absolute;
    inset: 0;
    background:
      radial-gradient(ellipse at 20% 30%, var(--leaf-bg-light) 0%, transparent 55%),
      radial-gradient(ellipse at 80% 75%, var(--leaf-bg-deep) 0%, transparent 60%),
      var(--leaf-bg);
  }

  /* Business name */
  .brand {
    position: absolute;
    left: 63px;
    top: 60px;
    width: 512px;
    height: 200px;
    margin: 0;
    display: flex;
    flex-direction: column;
    align-items: center;
    justify-content: center;
    font-family: "Montserrat", sans-serif;
    font-weight: 800;
    font-size: 62px;
    line-height: 1.1;
    color: var(--forest);
  }

  /* Credentials box */
  .credentials {
    position: absolute;
    left: 114px;
    top: 342px;
    width: 424px;
    height: 225px;
    background: var(--forest);
    color: var(--white);
    text-align: center;
  }
  .credentials .by {
    position: absolute;
    top: 26px; left: 0; right: 0;
    font-size: 23px;
    font-weight: 500;
  }
  .credentials .owner {
    position: absolute;
    top: 58px; left: 0; right: 0;
    font-family: "Bebas Neue", sans-serif;
    font-size: 76px;
    line-height: 1;
    color: var(--lime);
    letter-spacing: 0.5px;
  }
  .credentials .qualification {
    position: absolute;
    top: 131px; left: 0; right: 0;
    font-size: 27px;
    font-weight: 500;
    line-height: 34px;
  }

  /* Contact pills */
  .contact-pill {
    position: absolute;
    left: 86px;
    width: 480px;
    height: 90px;
    border-radius: 45px;
    background: var(--forest);
    color: var(--white);
  }
  .contact-pill svg { position: absolute; }
  .contact-email { top: 578px; }
  .contact-email .icon { left: 22px; top: 25px; }
  .contact-email .value {
    position: absolute;
    left: 89px; top: 24px;
    font-size: 22.5px;
    font-weight: 500;
  }
  .contact-phone { top: 677px; }
  .contact-phone .icon { left: 16px; top: 16px; }
  .contact-phone .value {
    position: absolute;
    left: 88px; top: 8px;
    font-size: 58px;
    font-weight: 600;
    letter-spacing: 1px;
  }
  .abn {
    position: absolute;
    left: 190px;
    top: 780px;
    font-size: 27px;
    font-weight: 500;
    color: var(--forest-text);
  }

  /* Service steps */
  .services {
    position: absolute;
    left: 741px;
    top: 65px;
    margin: 0;
    padding: 0;
    list-style: none;
  }
  .service {
    position: absolute;
    left: 0;
    display: flex;
    align-items: center;
    width: 420px;
  }
  .service:nth-child(1) { top: 0; }
  .service:nth-child(2) { top: 105px; }
  .service:nth-child(3) { top: 209px; }
  .service:nth-child(4) { top: 314px; }
  .service-badge {
    width: 90px;
    height: 90px;
    border-radius: 50%;
    background: var(--forest);
    display: flex;
    align-items: center;
    justify-content: center;
    flex: none;
  }
  .service-label {
    margin-left: 20px;
    font-size: 40px;
    font-weight: 800;
    letter-spacing: 1.5px;
    color: var(--forest-text);
  }

  /* Enjoy */
  .enjoy {
    position: absolute;
    left: 705px;
    top: 480px;
    width: 424px;
    height: 110px;
  }
  .enjoy .rule {
    position: absolute;
    top: 47px;
    width: 106px;
    height: 5px;
    background: var(--forest);
  }
  .enjoy .rule.left { left: 0; }
  .enjoy .rule.right { right: 0; }
  .enjoy .word {
    position: absolute;
    left: 0; right: 0; top: -8px;
    text-align: center;
    font-family: "Kaushan Script", cursive;
    font-size: 86px;
    line-height: 1.1;
    color: var(--forest);
  }

  .pitch {
    position: absolute;
    left: 680px;
    top: 614px;
    width: 470px;
    margin: 0;
    text-align: center;
    white-space: nowrap;
    font-size: 22.5px;
    font-weight: 500;
    line-height: 30px;
    color: var(--ink-green);
  }
</style>
</head>
<body>
<main class="flier">
  <div class="foliage-backdrop" role="img" aria-label="Soft green background of scattered leaves and trailing vines"></div>

  <h1 class="brand">
    <span>Parterre</span>
    <span>Gardens</span>
  </h1>

  <section class="credentials">
    <div class="by">by</div>
    <div class="owner">AARON WHITLOCK</div>
    <div class="qualification">Certificate 3, Horticulture.<br>Vale College, NSW</div>
  </section>

  <div class="contact-pill contact-email">
    <svg class="icon" width="46" height="34" viewBox="0 0 46 34" aria-hidden="true">
      <rect x="0" y="0" width="46" height="34" fill="var(--lime)"/>
      <path d="M2 2 L23 20 L44 2 M2 32 L17 15 M44 32 L29 15" fill="none" stroke="var(--forest)" stroke-width="3"/>
    </svg>
    <span class="value">aaron@parterregardens.com.au</span>
  </div>

  <div class="contact-pill contact-phone">
    <svg class="icon" width="60" height="60" viewBox="0 0 24 24" aria-hidden="true">
      <path fill="var(--lime)" d="M6.6 10.8a15.1 15.1 0 0 0 6.6 6.6l2.2-2.2c.3-.3.7-.4 1-.2 1.1.4 2.3.6 3.6.6.6 0 1 .4 1 1V20c0 .6-.4 1-1 1A17 17 0 0 1 3 4c0-.6.4-1 1-1h3.5c.6 0 1 .4 1 1 0 1.3.2 2.5.6 3.6.1.3 0 .7-.2 1l-2.3 2.2z"/>
    </svg>
    <span class="value">0412-305918</span>
  </div>

  <div class="abn">ABN: 51827394620</div>

  <ul class="services">
    <li class="service">
      <span class="service-badge">
        <svg width="44" height="44" viewBox="0 0 44 44" aria-hidden="true" fill="none" stroke="var(--white)" stroke-width="3">
          <circle cx="22" cy="10" r="7"/><circle cx="22" cy="34" r="7"/>
          <circle cx="10" cy="22" r="7"/><circle cx="34" cy="22" r="7"/>
          <circle cx="22" cy="22" r="5" fill="var(--forest)"/>
        </svg>
      </span>
      <span class="service-label">DESIGN</span>
    </li>
    <li class="service">
      <span class="service-badge">
        <svg width="52" height="52" viewBox="0 0 52 52" aria-hidden="true" fill="none" stroke="var(--white)" stroke-width="2.5" stroke-linejoin="round" stroke-linecap="round">
          <path d="M26 32 V16"/>
          <path d="M26 22 C18 22 12 16 12 8 C20 8 26 14 26 22 Z"/>
          <path d="M26 20 C26 12 32 6 40 6 C40 14 34 20 26 20 Z"/>
          <path d="M6 40 L16 34 H28 C30 34 30 38 28 38 H20 M28 38 L42 32 C45 31 46 35 43 37 L28 46 H12 L6 48"/>
        </svg>
      </span>
      <span class="service-label">INSTALL</span>
    </li>
    <li class="service">
      <span class="service-badge">
        <svg width="58" height="58" viewBox="0 0 58 58" aria-hidden="true" fill="none" stroke="var(--white)" stroke-width="2.5" stroke-linejoin="round" stroke-linecap="round">
          <path d="M6 22 L24 12 L34 32 L16 40 Z"/>
          <path d="M10 20 C8 14 12 8 18 10"/>
          <path d="M32 28 L42 32 L46 40"/>
          <path d="M46 46 v3 M50 46 v3 M46 53 v2 M50 53 v2"/>
        </svg>
      </span>
      <span class="service-label">GROW</span>
    </li>
    <li class="service">
      <span class="service-badge">
        <svg width="56" height="56" viewBox="0 0 56 56" aria-hidden="true" fill="none" stroke="var(--white)" stroke-width="2.5" stroke-linejoin="round" stroke-linecap="round">
          <path d="M20 6 L24 10 L28 4 L32 10 L36 6 V16 C36 21 32 23 28 23 C24 23 20 21 20 16 Z"/>
          <path d="M28 23 V46"/>
          <path d="M28 38 C22 38 18 34 18 30 C24 30 28 33 28 38 Z"/>
          <path d="M28 34 C28 29 32 26 38 26 C38 31 34 34 28 34 Z"/>
          <path d="M6 48 C16 44 40 44 50 48"/>
        </svg>
      </span>
      <span class="service-label">TEND</span>
    </li>
  </ul>

  <div class="enjoy">
    <span class="rule left"></span>
    <span class="word">Enjoy</span>
    <span class="rule right"></span>
  </div>

  <p class="pitch">All your gardening &amp; Landscaping<br>needs from design &amp; installation to<br>general maintenance.<br>Bespoke vegetable gardens &amp;<br>potager dsigns created to suit your<br>site &amp; requirements</p>
</main>
</body>
</html>
```